Junior tennis development pathway graphic

The National Racquet Guild Assn.(NRGA) and the Global Court Sports Union (GCSU)
recommend (read demand) that all junior tennis programs now be ran using a progressive format of 4 different colored balls, different court sizes and scoring systems for various ages. We want to create a graphic for our juniors page on our web site that will show parents in a VERY EASY to understand way how their kids will progress through the various stages of tennis. The page is being built using Bootstrap and we plan to use jQuerry Hotspot to give detailed information over certain areas of the graphic. This specific information will be Dbase driven with class names,and specific class info. - The design does not need to show this, I just though it might be helpful to know
Updates

There are 2 other sites that will be helpful in understanding this project:

The first is www.smallcourtstarters.example and the second is my junior page on my current website
www.pinecrestracquetclub.example/juniora.cfm

I added a new file named jr pathway 2

This is an idea i had for the project - needs to be completed and given some sizzle

Target Market(s)

Parents of children ages 3-16

Industry/Entity Type

Progressive

Requirements
Must have
• Vector format
800x800 pixels max
EASY TO UNDERSTAND
Use of some or all of the key words and phrases in the uploaded file "keywords"
Should not have
• I do not want it to look like every other development graphic already out there.
To see what is currently being used image search
"tennis pathway" or "junior tennis pathway"

"pathway and" juniorspathway" in the uploaded files section are 2 ideas of VERY bad attempts

```html
<!DOCTYPE html>
<html lang="en">
<head>
<meta charset="utf-8">
<title>4 Colors One Game – Junior Tennis Pathway</title>
<link rel="stylesheet" href="https://fonts.googleapis.com/css2?family=Montserrat:wght@600;700;800&display=swap">
<style>
  :root {
    --red-top: #ea343b;
    --red-bottom: #d21f27;
    --orange-top: #f58a3c;
    --orange-bottom: #e7632a;
    --green-top: #629c3a;
    --green-bottom: #377126;
    --yellow-top: #f8db38;
    --yellow-bottom: #eac21c;
    --ink: #ffffff;
    --ball-lime: #c9dc2c;
    --watermark: rgba(255, 255, 255, 0.3);
  }
  * { box-sizing: border-box; margin: 0; padding: 0; }
  html, body { width: 1200px; height: 1200px; overflow: hidden; background: #ffffff; }
  body { font-family: "Montserrat", Arial, sans-serif; color: var(--ink); }

  .pathway { position: relative; width: 1200px; height: 1200px; overflow: hidden; }

  .stage { position: absolute; overflow: hidden; }
  .stage--red    { left: 0;     top: 0;     width: 600px; height: 647px; background: linear-gradient(180deg, var(--red-top), var(--red-bottom)); }
  .stage--orange { left: 600px; top: 0;     width: 600px; height: 647px; background: linear-gradient(180deg, var(--orange-top), var(--orange-bottom)); }
  .stage--green  { left: 0;     top: 647px; width: 600px; height: 553px; background: linear-gradient(180deg, var(--green-top), var(--green-bottom)); }
  .stage--yellow { left: 600px; top: 647px; width: 600px; height: 553px; background: linear-gradient(180deg, var(--yellow-top), var(--yellow-bottom)); }

  .watermark {
    position: absolute;
    font-weight: 700;
    color: var(--watermark);
    line-height: 1;
    white-space: nowrap;
  }
  .watermark--learn { left: 38px;  top: 510px; font-size: 158px; letter-spacing: -6px; }
  .watermark--play  { left: 125px; top: 510px; font-size: 158px; letter-spacing: -8px; }
  .watermark--compete { top: 341px; font-size: 250px; letter-spacing: -8px; }
  .watermark--compete-left  { left: 12px; }
  .watermark--compete-right { left: -588px; }

  .headline { position: absolute; left: 0; top: 0; width: 1200px; height: 280px; }
  .headline__number {
    position: absolute; left: 213px; top: 8px;
    font-size: 300px; font-weight: 800; line-height: 1; letter-spacing: -6px;
    transform: scaleX(0.8); transform-origin: left top;
  }
  .headline__colors {
    position: absolute; left: 378px; top: 32px;
    font-size: 130px; font-weight: 700; line-height: 1; letter-spacing: -2px;
  }
  .headline__game {
    position: absolute; left: 452px; top: 152px;
    font-size: 90px; font-weight: 700; line-height: 1; letter-spacing: -1px;
  }
  .headline__tagline {
    position: absolute; left: 458px; top: 246px;
    font-size: 18.5px; font-weight: 600; letter-spacing: 0.1px; white-space: nowrap;
  }

  .player { position: absolute; border-radius: 40% 40% 30% 30%; }
  .player--red    { left: 72px;  top: 230px; width: 228px; height: 315px; background: radial-gradient(ellipse at center, rgba(255,255,255,0.22), rgba(255,255,255,0.04) 70%); }
  .player--orange { left: 966px; top: 208px; width: 234px; height: 376px; background: radial-gradient(ellipse at center, rgba(40,90,190,0.25), rgba(255,255,255,0.04) 70%); }
  .player--green  { left: 262px; top: 715px; width: 262px; height: 398px; background: radial-gradient(ellipse at center, rgba(255,255,255,0.28), rgba(255,255,255,0.04) 70%); }
  .player--yellow { left: 671px; top: 688px; width: 278px; height: 452px; background: radial-gradient(ellipse at center, rgba(236,90,150,0.3), rgba(255,255,255,0.04) 70%); }

  .ball { position: absolute; width: 58px; height: 58px; }
  .ball--red    { left: 348px; top: 304px; }
  .ball--orange { left: 715px; top: 304px; }
  .ball--green  { left: 64px;  top: 749px; }
  .ball--yellow { left: 956px; top: 749px; }

  .level { position: absolute; font-size: 26px; font-weight: 600; line-height: 47px; }
  .level--red    { left: 326px; top: 374px; }
  .level--orange { left: 702px; top: 374px; }
  .level--green  { left: 51px;  top: 836px; }
  .level--yellow { left: 946px; top: 836px; }
  .level__line { display: block; white-space: nowrap; }
  .level__line--wrap { line-height: 36px; margin-top: -4px; }
</style>
</head>
<body>
<main class="pathway">

  <section class="stage stage--red">
    <span class="watermark watermark--learn">LEARN</span>
  </section>
  <section class="stage stage--orange">
    <span class="watermark watermark--play">PLAY</span>
  </section>
  <section class="stage stage--green">
    <span class="watermark watermark--compete watermark--compete-left">COMPETE</span>
  </section>
  <section class="stage stage--yellow">
    <span class="watermark watermark--compete watermark--compete-right">COMPETE</span>
  </section>

  <header class="headline">
    <span class="headline__number">4</span>
    <span class="headline__colors">COLORS</span>
    <span class="headline__game">ONE GAME</span>
    <span class="headline__tagline">YOUR CHILD’S PATH TO SUCCESS AT EVERY LEVEL</span>
  </header>

  <div class="player player--red" role="img" aria-label="Illustration of a young boy in a red and orange outfit hitting a backhand"></div>
  <div class="player player--orange" role="img" aria-label="Illustration of a girl in a blue tennis dress preparing a forehand"></div>
  <div class="player player--green" role="img" aria-label="Illustration of a boy in a white cap and green shorts ready to return"></div>
  <div class="player player--yellow" role="img" aria-label="Illustration of a girl in a pink top hitting a forehand"></div>

  <svg class="ball ball--red" viewBox="0 0 58 58" aria-hidden="true">
    <circle cx="29" cy="29" r="27" fill="#e8262e" stroke="#ffffff" stroke-width="2"/>
    <path d="M8 12 A27 27 0 0 0 22 55 C14 42 14 26 8 12 Z" fill="var(--ball-lime)"/>
    <path d="M8 12 C16 26 16 42 22 55" fill="none" stroke="#ffffff" stroke-width="2.5"/>
  </svg>
  <svg class="ball ball--orange" viewBox="0 0 58 58" aria-hidden="true">
    <circle cx="29" cy="29" r="27" fill="#f06326" stroke="#ffffff" stroke-width="2"/>
    <path d="M8 12 A27 27 0 0 0 22 55 C14 42 14 26 8 12 Z" fill="var(--ball-lime)"/>
    <path d="M8 12 C16 26 16 42 22 55" fill="none" stroke="#ffffff" stroke-width="2.5"/>
  </svg>
  <svg class="ball ball--green" viewBox="0 0 58 58" aria-hidden="true">
    <circle cx="29" cy="29" r="27" fill="#6aa531" stroke="#ffffff" stroke-width="2"/>
    <path d="M8 12 A27 27 0 0 0 22 55 C14 42 14 26 8 12 Z" fill="var(--ball-lime)"/>
    <path d="M8 12 C16 26 16 42 22 55" fill="none" stroke="#ffffff" stroke-width="2.5"/>
  </svg>
  <svg class="ball ball--yellow" viewBox="0 0 58 58" aria-hidden="true">
    <circle cx="29" cy="29" r="27" fill="#f5e21c" stroke="#ffffff" stroke-width="2"/>
    <path d="M8 12 A27 27 0 0 0 22 55 C14 42 14 26 8 12 Z" fill="var(--ball-lime)"/>
    <path d="M8 12 C16 26 16 42 22 55" fill="none" stroke="#ffffff" stroke-width="2.5"/>
  </svg>

  <div class="level level--red">
    <span class="level__line">Red Ball</span>
    <span class="level__line">4–8 years old</span>
    <span class="level__line">19–23 inch racquet</span>
  </div>
  <div class="level level--orange">
    <span class="level__line">Orange Ball</span>
    <span class="level__line">7–10 years old</span>
    <span class="level__line">23–25 inch racquet</span>
  </div>
  <div class="level level--green">
    <span class="level__line">Green Ball</span>
    <span class="level__line">10–12 years old</span>
    <span class="level__line">26–27 inch racquet</span>
  </div>
  <div class="level level--yellow">
    <span class="level__line">Yellow Ball</span>
    <span class="level__line">13 years and up</span>
    <span class="level__line">27 inch (adult)</span>
    <span class="level__line level__line--wrap">racquet</span>
  </div>

</main>
</body>
</html>
```